Neue Website fuer Software-Firma (CMS: Joomla, Responsive Design)
Zielgruppe
Die VANTRIX ist ein Software- und Beratungshaus im Lager- und Produktionslogistikbereich. Unsere Kunden sind Industriefirmen und Logistikdienstleister, die ein oder mehrere Laeger bewirtschaften und dafuer eine Software und mobile Datenerfassung einsetzen. Fast alle unserer Kunden haben KVT im Einsatz.
Aufgabenstellung
Unsere aktuelle Website wurde seit langem nicht mehr gepflegt und ist veraltet.
Wir moechten die neue Website gern mit dem CMS Joomla betreiben (ggf. waere auch Wordpress moeglich). Gern koennen Sie als Basis ein bereits existierendes (freies) Theme verwenden, wenn es entweder bereits alle Ansprueche erfuellt oder Sie es entsprechend anpassen.
Die neue Website soll in jedem Fall responsive sein, d.h. sowohl auf Desktop, Tablet und Smartphone funktionieren und das Design entsprechend anpassen.
Unsere aktuelle Seite steht unter www.vantrix-lagerwerk.example
Eine Seite, die uns besonders gut gefaellt, ist www.quendal.example (die sich auch teilweise an die gleichen Kunden richtet).
Wir moechten ein klares Design. Ein Beispiel, wie eines unserer Dashboards unserer Software aussieht, finden Sie anbei. Die Farbgestaltung darin wird jedoch noch geaendert. Sie wird eher in Richtung der Farbgestaltung der Quendal-Website gehen, jedoch immer noch grundsaetzlich hell sein. Evtl. koennen Sie Elemente daraus aufgreifen? Es soll in jedem Fall ersichtlich sein, dass Website und Software von der gleichen Firma sind.
Es soll moeglichst viel mit Grafiken gearbeitet werden – aehnlich der Quendal-Seite unter der Dia-Show. Diese muessen aber nicht zwingend farbig sein. Ein Mockup fuer einfarbige Grafiken unterhalb einer Diashow habe ich hier erstellt: https://helgard07.seitenbau.example/meinewebsite-1 Bitte orientieren Sie sich aber nicht an dieser Seite selbst – das war nur ein Probierbeispiel.
Desweiteren soll die Seite suchmaschinenfreundlich sein.
In Ihren Leistungen enthalten sein soll:
- Erstellung der Homepage incl.
o Menu (wie bei Quendal soll es ausklappbar sein und mind. 2 Ebenen koennen)
o Login-Button der einen externen Link aufruft
o Auswahl der Sprache (und damit Verlinkung zu jeweils der Homepage in der
ausgewaehlten Sprache
o Moeglichkeit zum Chat
o Suchfeld zum Durchsuchen aller S..

```html
<!DOCTYPE html>
<html lang="en">
<head>
<meta charset="utf-8">
<title>VANTRIX – Our Mission</title>
<link href="https://fonts.googleapis.com/css2?family=Lato:ital,wght@0,300;0,400;0,700;1,300&display=swap" rel="stylesheet">
<style>
:root{
  --page:#f1f4f7;
  --white:#ffffff;
  --navy:#1a3a8f;
  --red:#d20a0a;
  --dark:#141f2c;
  --text:#3a3f47;
  --muted:#8a9099;
  --line:#e2e5ea;
  --social:#b9c3cf;
}
*{box-sizing:border-box;margin:0;padding:0}
html,body{width:971px;height:1200px;overflow:hidden}
body{position:relative;background:var(--page);font-family:"Lato",sans-serif;font-weight:300;color:var(--text)}
.abs{position:absolute}

/* header */
.site-header{left:0;top:0;width:971px;height:45px;background:var(--page);border-bottom:1px solid var(--red)}
.brand{left:199px;top:10px;font-weight:700;font-size:20px;letter-spacing:.5px;color:var(--navy)}
.brand-tag{left:199px;top:32px;font-size:5px;color:var(--navy);letter-spacing:.3px}
.divider{top:0;width:1px;height:44px;background:var(--line)}
.menu-toggle{left:307px;top:16px;display:flex;align-items:center;gap:10px;font-size:9.5px;font-weight:400;color:var(--dark)}
.util{top:17px;display:flex;align-items:center;gap:6px;font-size:8px;font-weight:400;color:var(--text)}
.social{display:flex;gap:2px}
.social span{width:15px;height:15px;background:var(--social)}

/* hero */
.hero{left:84px;top:46px;width:799px;height:319px;background:linear-gradient(90deg,#1e44ab 0%,#3454a8 30%,#7d7f96 55%,#c4a57d 78%,#d7bb92 100%)}
.hero-title{left:226px;top:150px;font-size:28px;line-height:29px;color:var(--white);font-weight:300}
.btn-contact{left:229px;top:251px;width:131px;height:25px;background:var(--red);color:var(--white);font-size:12.5px;font-weight:300;display:flex;align-items:center;justify-content:center}
.dots{left:469px;top:339px;display:flex;gap:4px}
.dots span{width:4px;height:4px;border-radius:50%;background:rgba(255,255,255,.55)}
.dots span:first-child{background:#fff}

/* tabs */
.tabs{left:84px;top:365px;width:799px;height:60px;background:var(--white);border-bottom:1px solid var(--line)}
.tab{top:22px;font-size:13.5px;color:var(--navy);font-weight:300}
.tab.active{color:var(--red)}
.tab-underline{left:373px;top:58px;width:96px;height:1px;background:var(--red)}

/* content */
.content{left:84px;top:425px;width:799px;height:546px;background:var(--white)}
.section-title{font-size:18px;color:var(--navy);font-weight:300}
.section-lead{font-size:10px;font-style:italic;color:var(--muted);white-space:nowrap}
.section-body{font-size:8px;line-height:9.6px;color:var(--text);white-space:nowrap}

/* experts */
.experts{left:84px;top:971px;width:799px;height:63px;background:var(--dark)}
.experts-label{left:0;top:0;width:205px;height:63px;background:var(--red);color:var(--white);font-size:15.5px;line-height:18px;padding:13px 0 0 118px}
.expert{top:15px;width:110px;margin-left:-55px;text-align:center;color:var(--white);font-size:8.3px;font-weight:300;letter-spacing:.2px}
.expert svg{display:block;margin:0 auto 5px}

/* chat */
.chat-btn{left:884px;top:599px;width:44px;height:44px;background:var(--red);display:flex;align-items:center;justify-content:center}

/* footer */
.footer{left:84px;top:1034px;width:799px;height:135px;background:var(--white)}
.f-col{top:23px}
.f-head{font-size:8px;color:var(--red);font-weight:400;margin-bottom:8px}
.f-list{list-style:none;font-size:7.6px;line-height:12px;color:var(--text);padding-left:1px}
.f-text{font-size:7.6px;line-height:9.5px;color:var(--text);padding-left:1px;white-space:nowrap}
.f-text .mail{color:var(--red)}
.legal{top:1177px;font-size:7.6px;color:var(--muted)}
</style>
</head>
<body>

<header class="site-header abs">
  <div class="brand abs">VANTRIX</div>
  <div class="brand-tag abs">Software Solutions For Logistics</div>
  <div class="divider abs" style="left:295px"></div>
  <div class="divider abs" style="left:368px"></div>
  <div class="menu-toggle abs">
    <svg width="19" height="13" viewBox="0 0 19 13"><rect y="0" width="19" height="2" fill="#141f2c"/><rect y="5.5" width="19" height="2" fill="#141f2c"/><rect y="11" width="19" height="2" fill="#141f2c"/></svg>
    <span>Menu</span>
  </div>
  <div class="util abs" style="left:572px">
    <svg width="13" height="13" viewBox="0 0 13 13" fill="none" stroke="#3a3f47" stroke-width=".8"><circle cx="6.5" cy="4" r="3"/><path d="M1 12.5c0-3 2.5-5 5.5-5s5.5 2 5.5 5z"/></svg>
    <span>Login</span>
  </div>
  <div class="util abs" style="left:636px">
    <svg width="13" height="13" viewBox="0 0 13 13" fill="none" stroke="#3a3f47" stroke-width=".8"><circle cx="6.5" cy="6.5" r="6"/><path d="M2 3.5l2.5 1.5 0 2.5 2 1-1 3M8 1l-.5 2.5 2 1.5 2.5-.5M9 12l.5-3 2.5-1"/></svg>
    <span>Language</span>
  </div>
  <div class="social abs" style="left:726px;top:15px"><span></span><span></span><span></span></div>
</header>

<div class="hero abs" role="img" aria-label="Photo of two warehouse staff checking paperwork among cardboard boxes, with a blue overlay on the left"></div>
<h1 class="hero-title abs">Our Management is<br>commited to solve your<br>internal logistics problems</h1>
<div class="btn-contact abs">CONTACT US</div>
<div class="dots abs"><span></span><span></span><span></span><span></span></div>

<nav class="tabs abs">
  <span class="tab abs" style="left:124px">About Company</span>
  <span class="tab abs" style="left:250px">Our Philosophie</span>
  <span class="tab active abs" style="left:385px">Our Mission</span>
  <span class="tab abs" style="left:497px">Team</span>
  <div class="tab-underline abs"></div>
</nav>

<main class="content abs">
  <h2 class="section-title abs" style="left:120px;top:37px">Our Mission</h2>
  <p class="section-lead abs" style="left:121px;top:66px">Our top goal is clearly defined: your satisfaction.</p>
  <p class="section-body abs" style="left:121px;top:88px">Lorem Ipsum is simply dummy text of the printing and typesetting industry.<br>Lorem Ipsum has been the industry's standard dummy text ever since the<br>1500s, when an unknown printer took a galley of type and scrambled it to<br>make a type specimen book. It has survived not only five centuries, but also<br>the leap into electronic typesetting, remaining essentially unchanged. It was<br>popularised in the 1960s with the release of Printwell sheets containing<br>Lorem Ipsum passages, and more recently with desktop publishing software<br>like Layoutra including versions of Lorem Ipsum.<br>Lorem Ipsum is simply dummy text of the printing and typesetting industry.<br>Lorem Ipsum has been the industry's standard dummy text ever since the<br>1500s, when an unknown printer took a galley of type and scrambled it to<br>make dus Layoutra including versions of Lorem Ipsum.</p>
  <div class="abs" style="left:401px;top:30px;width:289px;height:221px;background:linear-gradient(100deg,#dfe4ea 0%,#c9d0d8 45%,#c7b79a 75%,#9a8c78 100%)" role="img" aria-label="Photo of a bright warehouse hall with tall pallet racking"></div>

  <div class="abs" style="left:116px;top:281px;width:284px;height:221px;background:linear-gradient(120deg,#cfe4f3 0%,#a9cde8 45%,#d7e9f5 100%)" role="img" aria-label="Photo of an industrial robot arm in a light blue automated production line"></div>
  <h2 class="section-title abs" style="left:429px;top:304px">Headline 2</h2>
  <p class="section-lead abs" style="left:430px;top:333px">Our top goal is clearly defined: your satisfaction.</p>
  <p class="section-body abs" style="left:430px;top:355px">Lorem Ipsum is simply dummy text of the printing and typesetting industry.<br>Lorem Ipsum has been the industry's standard dummy text ever since the<br>1500s, when an unknown printer took a galley of type and scrambled it to<br>make a type specimen book. It has survived not only five centuries, but also<br>the leap into electronic typesetting, remaining essentially unchanged. It was<br>popularised in the 1960s with the release of Printwell sheets containing<br>Lorem Ipsum passages, and more recently with desktop publishing software<br>like Layoutra including versions of Lorem Ipsum.<br>Lorem Ipsum is simply dummy text of the printing and typesetting industry.<br>Lorem Ipsum has been the industry's standard dummy text ever since the<br>1500s, when an unknown printer took a galley of type and scrambled it to<br>make dus Layoutra including versions of Lorem Ipsum.</p>
</main>

<section class="experts abs">
  <div class="experts-label abs">We are<br>Experts in:</div>
  <div class="expert abs" style="left:288px">
    <svg width="22" height="20" viewBox="0 0 22 20" fill="none" stroke="#fff" stroke-width=".9"><path d="M2 6L11 1l9 5v13H2z"/><path d="M5 9h12M5 12h12M5 15h12M5 18h12"/></svg>PRODUCTION</div>
  <div class="expert abs" style="left:401px">
    <svg width="22" height="20" viewBox="0 0 22 20" fill="none" stroke="#fff" stroke-width=".9"><rect x="1.5" y="3" width="19" height="15"/><path d="M8 3v6l3-1.5L14 9V3M13 13h5M13 15.5h5"/></svg>WAREHOUSING</div>
  <div class="expert abs" style="left:513px">
    <svg width="26" height="20" viewBox="0 0 26 20" fill="none" stroke="#fff" stroke-width=".9"><path d="M7 17H5a4 4 0 0 1 0-8 6 6 0 0 1 11-3 5 5 0 0 1 6 6 3 3 0 0 1-1 5h-2"/><path d="M13 11l4 2v4l-4 2-4-2v-4zM9 13l4 2 4-2M13 15v4"/></svg>KVT</div>
  <div class="expert abs" style="left:626px">
    <svg width="26" height="20" viewBox="0 0 26 20" fill="none" stroke="#fff" stroke-width=".9"><path d="M9 14V8l6-4 3 3M4 2h6M7 2v6"/><circle cx="15" cy="4" r="1.5"/><rect x="6" y="14" width="6" height="2"/><path d="M2 18h22"/><circle cx="4" cy="18" r="1"/><circle cx="9" cy="18" r="1"/><circle cx="14" cy="18" r="1"/><circle cx="19" cy="18" r="1"/><circle cx="24" cy="18" r="1"/></svg>AUTOMATION</div>
</section>

<div class="chat-btn abs">
  <svg width="20" height="17" viewBox="0 0 20 17"><path d="M2 1h16a1 1 0 0 1 1 1v10a1 1 0 0 1-1 1H8l-4 3v-3H2a1 1 0 0 1-1-1V2a1 1 0 0 1 1-1z" fill="#fff"/><circle cx="6.5" cy="7" r="1.2" fill="#d20a0a"/><circle cx="10" cy="7" r="1.2" fill="#d20a0a"/><circle cx="13.5" cy="7" r="1.2" fill="#d20a0a"/></svg>
</div>

<footer class="footer abs">
  <div class="f-col abs" style="left:120px">
    <div class="f-head">Company</div>
    <ul class="f-list"><li>About us</li><li>Services</li><li>Contact us</li><li>Career</li><li>Last News</li><li>Clients</li><li>FAQ</li></ul>
  </div>
  <div class="f-col abs" style="left:216px">
    <div class="f-head">Services</div>
    <ul class="f-list"><li>KVT Development</li><li>Warehouse Management</li><li>Automation / Integration</li><li>Product number 4</li><li>Product number 5</li></ul>
  </div>
  <div class="f-col abs" style="left:340px">
    <div class="f-head">United States</div>
    <p class="f-text">VANTRIX -<br>Software Solutions For Logistics, Inc.<br>240 Harlow Ridge Ave., Suite 310<br>Brenford, MI 48290<br><span class="mail">info@vantrix-lagerwerk.example</span><br>Tel: +1 555 014 2260<br>Fax: +1 555 014 2298</p>
  </div>
  <div class="f-col abs" style="left:491px">
    <div class="f-head">Germany</div>
    <p class="f-text">VANTRIX GmbH -<br>Softwareloesungen der Logistik<br>Werkstrasse 14<br>61450 Altenbrunn<br><span class="mail">info@vantrix-lagerwerk.example</span><br>Tel: +49 6100 555010<br>Fax: +49 6100 555019</p>
  </div>
  <div class="social abs" style="left:635px;top:22px"><span></span><span></span><span></span></div>
</footer>

<div class="legal abs" style="left:209px">Impring &nbsp;&nbsp; AGB</div>
<div class="legal abs" style="left:627px">© 2017 by VANTRIX GmbH / VANTRIX Inc.</div>

</body>
</html>
```